Willowmere Counseling (Endure - Mend - Flourish) - Double Sided Business Card

I would like a 2-sided business card. Front: Matte Black or Navy with Logo & Tagline. Back: Name, Address, Phone Number, Email, & Website (maybe would like to include a small map pin-pointing location); Prefer front to be a gold/silver foil (iridescent); Back prefer white or light colored background with lettering that is easy to read and simple

Target Market(s)

Individuals & Couples (13 y.o. - ALL Adults); High end clientele

Industry/Entity Type

Licensed Professional Counselor (Mental Health)

Contact Information for Business Card

Name: Willowmere Counseling; Tagline: Endure - Mend - Flourish; Address: 3870 N. Garrick Ave., Suite 214, Fort Worth, TX 76132; Phone: (214) 555-0187; Website: www.WillowmereCounseling.example

Font styles to use
Serif

Requirements
Must have
• Logo on Front (Large) prefer gold/silver foil on a matte dark color (i.e. black, navy, etc.); Back of Card: All other relevant information

```html
<!DOCTYPE html>
<html lang="en">
<head>
<meta charset="utf-8">
<title>Willowmere Counseling – Business Card</title>
<link rel="stylesheet" href="https://fonts.googleapis.com/css2?family=Cinzel:wght@500;600&family=Arimo:wght@400;700&display=swap">
<style>
  :root {
    --page: #e8e8e6;
    --card-dark: #2f3033;
    --map-grey: #575a60;
    --map-grey-light: #62656b;
    --gold: #d7b74f;
    --white: #ffffff;
    --ink: #2a2a2c;
  }
  * { box-sizing: border-box; margin: 0; padding: 0; }
  html, body {
    width: 1200px; height: 801px; overflow: hidden;
    background: var(--page);
    font-family: "Arimo", Arial, sans-serif;
  }
  .sheet { position: relative; width: 1200px; height: 801px; }

  .card {
    position: absolute; top: 258px;
    width: 500px; height: 286px;
    overflow: hidden;
    box-shadow: 0 6px 18px rgba(0,0,0,.18);
  }
  .card--front { left: 70px; background: var(--card-dark); }
  .card--back  { left: 630px; background: var(--map-grey); }

  /* front */
  .front-edge { position: absolute; left: 0; bottom: 0; width: 500px; height: 22px; }

  .brand {
    position: absolute; top: 48px; right: 34px;
    display: flex; align-items: center; gap: 12px;
  }
  .brand__dot { width: 34px; height: 34px; border-radius: 50%; background: var(--gold); }
  .brand__name {
    font-family: "Cinzel", "Times New Roman", serif;
    font-weight: 600; font-size: 24px; line-height: 1.05;
    color: var(--gold); letter-spacing: .04em;
  }
  .brand__name span { display: block; }

  .address {
    position: absolute; top: 138px; right: 40px;
    display: flex; align-items: flex-end; gap: 8px;
    color: var(--white); font-size: 13px; line-height: 1.35;
  }
  .address svg { width: 11px; height: 14px; margin-bottom: 2px; }

  .person {
    position: absolute; left: 34px; bottom: 42px;
    color: var(--white);
  }
  .person__name { color: var(--gold); font-weight: 700; font-size: 17px; letter-spacing: .03em; }
  .person__role { font-size: 13px; margin-bottom: 10px; }
  .contact { display: flex; align-items: center; gap: 8px; font-size: 13px; margin-top: 4px; }
  .contact svg { width: 12px; height: 12px; }

  /* back */
  .map {
    position: absolute; inset: 0;
    background: linear-gradient(160deg, var(--map-grey-light), var(--map-grey));
  }
  .tagline-band {
    position: absolute; left: 0; right: 0; top: 196px; height: 34px;
    background: var(--gold);
    display: flex; align-items: center; justify-content: center;
  }
  .tagline {
    font-family: "Cinzel", "Times New Roman", serif;
    font-weight: 600; font-size: 16px; color: var(--ink); letter-spacing: .05em;
  }
  .back-edge-left { position: absolute; left: 0; top: 0; bottom: 0; width: 4px; background: var(--gold); }
  .back-edge-bottom { position: absolute; left: 0; right: 0; bottom: 0; height: 4px; background: var(--gold); }
</style>
</head>
<body>
<main class="sheet">

  <section class="card card--front" aria-label="Card front">
    <div class="brand">
      <div class="brand__dot"></div>
      <div class="brand__name"><span>Willowmere</span><span>Counseling</span></div>
    </div>

    <div class="address">
      <svg viewBox="0 0 11 14" aria-hidden="true"><path d="M5.5 0A5.5 5.5 0 0 0 0 5.5C0 9 5.5 14 5.5 14S11 9 11 5.5A5.5 5.5 0 0 0 5.5 0Zm0 7.6a2.1 2.1 0 1 1 0-4.2 2.1 2.1 0 0 1 0 4.2Z" fill="#d7b74f"/></svg>
      <p>3870 N. Garrick Ave., Suite 214<br>Fort Worth, TX 76132</p>
    </div>

    <div class="person">
      <p class="person__name">MARCUS DELANEY</p>
      <p class="person__role">Manager</p>
      <p class="contact">
        <svg viewBox="0 0 12 12" aria-hidden="true"><path d="M2.4 0.6 4.2 2.6 3.3 4.2c.8 1.7 2 2.9 3.6 3.6l1.5-.9 2 1.8-.9 2.1C5.2 10.6 1.2 6.6.4 1.5Z" fill="#d7b74f"/></svg>
        (214) 555-0187
      </p>
      <p class="contact">
        <svg viewBox="0 0 12 12" aria-hidden="true"><circle cx="6" cy="6" r="5.2" fill="none" stroke="#d7b74f" stroke-width="1.4"/><path d="M1 6h10M6 1c-2.4 2.8-2.4 7.2 0 10M6 1c2.4 2.8 2.4 7.2 0 10" fill="none" stroke="#d7b74f" stroke-width="1"/></svg>
        www.WillowmereCounseling.example
      </p>
    </div>

    <svg class="front-edge" viewBox="0 0 500 22" aria-hidden="true">
      <path d="M0 12H20V6H38V12H312V22H0Z" fill="#d7b74f"/>
      <path d="M312 12H320V2H500V22H312Z" fill="#ffffff"/>
    </svg>
  </section>

  <section class="card card--back" aria-label="Card back">
    <div class="map" role="img" aria-label="Dark grey street map showing the office location with nearby roads and a location pin"></div>
    <div class="tagline-band"><p class="tagline">Endure - Mend - Flourish</p></div>
    <div class="back-edge-left"></div>
    <div class="back-edge-bottom"></div>
  </section>

</main>
</body>
</html>
```